Custom Wordpress Theme - Original and Professional

We are a boutique IT consulting firm that provide small and medium business in Australia three different levels of IT service.
We are looking for a developer who will create a customised, original and professional wordpress theme. We are looking for the developer to create a professional, clean, clear and simple theme with a stylish layout, images and icons.
Our three services are: IT support | IT Services | IT Solutions and we would like to clearly differentiate the difference in each level of service in as few words as possible.
IT Support is the ad hock “call us, when you need us” service, that smaller business or those with minimal issues use.
IT service is the unlimited service, that business with existing (and well maintained) IT systems choose and is both flexible and scalable including no contracts or paperwork required.
IT solutions are the unlimited service that businesses that need new or updated infrastructure choose and it includes all the hardware, software and services with no contracts or any ongoing commitment.
The main page on the web site will attract the visitor to choose the right “service level” for their business and then we will have a dedicated page for each service and another page for a comparison (table) to compare all three services.
Lastly we will need a contact us page that has both office locations (Sydney and Melbourne), contact phone numbers and an email form.
Items we are focused on for this project are: 1. Images, 2.Icons 3. Layout.
In summary we are looking for a custom WordPress theme into a 6 page (Home, IT Support, IT Services, IT Solutions, Compare Service levels and Contact us) website. The design must include relevant images and icons and be clear, simple, professional and sleek.

Thank you for your time and creativity and I look forward to working with you!

Target Market(s)

Small and Medium businesses in Australia

Industry/Entity Type

Boutique

Requirements
Must have
• - 6 Pages layout: Home, IT support, IT services, IT Solutions, Compare service levels and Contact us
- Images, Layout and Icons.
- Clean, Clear, Simple, Elegant, Stylish.
Nice to have
• - Some text (if possible but not required).
Should not have
• - Complexity.
- Confusing layout.
- Generic non matching images and icons.

```html
<!DOCTYPE html>
<html lang="en">
<head>
<meta charset="utf-8">
<title>IT Services – Home</title>
<link rel="stylesheet" href="https://fonts.googleapis.com/css2?family=Open+Sans:wght@400;600;700&family=Arimo:wght@400;700&family=PT+Sans:wght@400;700&display=swap">
<style>
:root{
  --blue:#1a7fb8;
  --blue-dark:#24508f;
  --blue-light:#2aa3dc;
  --ink:#2b2b2b;
  --grey-text:#5a5a5a;
  --panel:#f2f2f2;
  --footer:#3a3a3a;
  --footer-bar:#555;
  --orange:#e8550f;
  --green:#6aa514;
  --link:#2aa8e0;
}
*{box-sizing:border-box;margin:0;padding:0}
html,body{width:966px;height:1200px;overflow:hidden;background:#fff}
body{position:relative;font-family:"Arimo",Arial,sans-serif;color:var(--ink)}
.abs{position:absolute}

/* header */
.logo{left:86px;top:20px;font:600 34px/1 "Open Sans",sans-serif;color:var(--blue)}
.phone{left:735px;top:17px;display:flex;align-items:center;gap:7px;font:700 17px "Open Sans",sans-serif;color:#444;letter-spacing:.5px}
.follow{left:678px;top:68px;display:flex;align-items:center;gap:6px;font:italic 15px "PT Sans",sans-serif;color:#333}
.follow i{display:block;width:22px;height:22px;border-radius:50%}

/* nav */
.navbar{left:0;top:99px;width:966px;height:72px;background:var(--blue)}
.nav{left:92px;top:93px;display:flex;height:44px;align-items:center;font:600 12.5px "Open Sans",sans-serif;color:#fff}
.nav a{color:#fff;text-decoration:none;padding:0 17px;border-left:1px solid rgba(255,255,255,.3)}
.nav a.home{background:linear-gradient(#444,#000);width:80px;height:44px;line-height:50px;text-align:center;border:0;border-radius:4px 4px 0 0;padding:0;margin-right:0}
.nav a.home+a{border-left:0;margin-left:14px}
.search{left:697px;top:106px;width:176px;height:28px;background:#fff;font:300 13px "Open Sans",sans-serif;color:#aaa;padding:6px 11px}
.search svg{position:absolute;right:5px;top:3px}

/* hero */
.bluewide{left:0;top:467px;width:966px;height:208px;background:linear-gradient(#2aa3dc,#24508f)}
.hero{left:86px;top:148px;width:794px;height:333px;background:#fff;box-shadow:0 0 3px rgba(0,0,0,.2)}
.hero-bg{left:88px;top:150px;width:560px;height:329px;background:linear-gradient(90deg,#f7f7f7,#e9ebee 70%,#dfe3e8)}
.hero-photo{left:540px;top:150px;width:338px;height:329px;background:linear-gradient(90deg,#e4e7eb,#cfd3d8 30%,#2c3038 75%,#1d2026)}
.hero h1{left:116px;top:186px;font:600 27px "Open Sans",sans-serif;color:var(--blue);letter-spacing:1px}
.hero-lead{left:110px;top:226px;width:370px;font:400 20.5px/27px "Open Sans",sans-serif;color:#555}
.hero-body{left:110px;top:313px;width:360px;font:10px/18px "Arimo",sans-serif;color:#444}
.btn-learn{left:111px;top:390px;width:87px;height:28px;background:linear-gradient(#f36d1c,#d9460c);border-radius:3px;color:#fff;font:600 12px/28px "Open Sans",sans-serif;text-align:center}
.dots{left:132px;top:444px;display:flex;gap:4px}
.dots i{width:10px;height:10px;border-radius:50%;background:#333}
.dots i.on{background:var(--blue-dark)}

/* service boxes */
.svc{top:505px;width:235px;height:137px;border:1px solid rgba(255,255,255,.75);color:#fff;font:10px/13px "Arimo",sans-serif}
.svc h2{font:600 18px "Open Sans",sans-serif;text-align:center;letter-spacing:1.5px;margin:9px 0 9px}
.svc .txt{text-align:center;padding:0 13px}
.svc ul{list-style:none;padding:0 12px}
.svc li{display:flex;align-items:flex-start;gap:7px;margin-bottom:6px}
.svc li svg{flex:none;margin-top:1px}
.svc .more{position:absolute;left:50%;bottom:-11px;transform:translateX(-50%);background:#fff;color:var(--blue-dark);font:600 12px/20px "Open Sans",sans-serif;padding:0 12px;border-radius:10px}

/* content */
.content{left:0;top:677px;width:966px;height:264px;background:var(--panel)}
.h3{font:400 17px "Open Sans",sans-serif;color:#333}
.news-title{left:105px;top:738px;font:600 13.5px "Open Sans",sans-serif;color:#333}
.news-date{left:105px;top:759px;font:10px "Open Sans",sans-serif;color:#777}
.news-body{left:105px;top:785px;width:225px;font:9.5px/18.5px "Open Sans",sans-serif;color:#333}
.news-more{left:105px;top:889px;font:10px "Open Sans",sans-serif;color:#555;letter-spacing:.5px}
.tweets{left:353px;top:740px;width:220px;height:175px;border:1px solid #ccc;background:#f4f4f4}
.tweet{padding:14px 14px 0;height:80px;font:9.5px/16px "Open Sans",sans-serif;color:#333}
.tweet+.tweet{border-top:1px solid #ccc;height:94px}
.tweet b{font-weight:400;color:#666}
.tweet small{display:block;margin-top:4px;font-size:8.5px;color:#777}
.quote{left:591px;top:740px;width:271px;height:142px;background:#fff;border:1px solid #ccc;padding:24px 28px;font:9.5px/18.5px "Open Sans",sans-serif;color:#333}
.quote .mark{position:absolute;right:14px;bottom:8px;font:700 22px Georgia,serif;color:#333}
.quote-by{left:735px;top:894px;font:10px "Open Sans",sans-serif;color:#333}
.quote-by span{color:var(--orange)}
.qdots{left:837px;top:726px;display:flex;gap:3px}
.qdots i{width:4px;height:4px;border-radius:50%;background:#ccc}

/* cta */
.cta{left:0;top:942px;width:966px;height:80px;background:var(--blue)}
.cta-big{left:97px;top:961px;font:700 29px "PT Sans",sans-serif;color:#fff;letter-spacing:-.3px}
.cta-small{left:460px;top:993px;font:700 14px "PT Sans",sans-serif;color:#fff}
.cta-btn{left:670px;top:961px;width:205px;height:41px;background:linear-gradient(#8cc81e,#5b960d);border:1px solid #fff;border-radius:3px;color:#fff;font:700 19px/39px "PT Sans",sans-serif;text-align:center}

/* footer */
.footer{left:0;top:1024px;width:966px;height:152px;background:var(--footer)}
.footbar{left:0;top:1175px;width:966px;height:25px;background:var(--footer-bar);color:#fff;font:9px/25px "PT Sans",sans-serif;text-align:center}
.mapframe{left:106px;top:1040px;width:137px;height:112px;border-radius:6px;background:#2e2e2e;box-shadow:inset 0 0 0 1px #555}
.map{left:120px;top:1051px;width:103px;height:89px;background:linear-gradient(135deg,#f4efcf,#e9e3b8 50%,#f2ecd3)}
.addr{font:8.6px/11px "PT Sans",sans-serif;color:#fff}
.addr b{color:var(--link);font-weight:700}
.ft-link{font:700 8.5px "PT Sans",sans-serif;color:var(--link)}
.soc{display:flex;gap:8px;align-items:flex-start}
.soc .ic{width:40px;height:40px;border-radius:6px;flex:none}
.soc .t{font:700 8.5px/11px "PT Sans",sans-serif;color:#fff}
.soc .t b{display:block;font-size:11.5px;line-height:13px;color:var(--link)}
.nl{left:720px;top:1060px;width:145px;height:22px;border-radius:11px;background:linear-gradient(#222,#4a4a4a);border:1px solid #666}
</style>
</head>
<body>

<header>
  <div class="abs logo">IT Services</div>
  <div class="abs phone">
    <svg width="20" height="20" viewBox="0 0 20 20"><rect width="20" height="20" rx="3" fill="#1a7fb8"/><path d="M6 4c1 0 2 2 2 3s-1 1-1 2c1 2 2 3 4 4 1 0 1-1 2-1s3 1 3 2-2 2-3 2C8 16 4 12 4 7c0-1 1-3 2-3z" fill="#fff"/></svg>
    403-555-0187
  </div>
  <div class="abs follow">Follow us on <i style="background:#3fa9e0"></i><i style="background:#e9601c"></i><i style="background:#23377a"></i><i style="background:#c9c9c9"></i></div>
</header>

<div class="abs navbar"></div>
<nav class="abs nav">
  <a class="home">Home</a><a>Job Search</a><a style="padding:0 28px">Benefits</a><a style="padding:0 22px">Locations</a><a>About Us</a><a>Contact Us</a>
</nav>
<div class="abs search">Search
  <svg width="24" height="24" viewBox="0 0 24 24"><circle cx="12" cy="12" r="10.5" fill="none" stroke="#1a7fb8" stroke-width="2"/><path d="M6 12h11M13 7l5 5-5 5" fill="none" stroke="#1a7fb8" stroke-width="2"/></svg>
</div>

<div class="abs bluewide"></div>
<section>
  <div class="abs hero"></div>
  <div class="abs hero-bg"></div>
  <div class="abs hero-photo" role="img" aria-label="Photo of a smiling businesswoman in a dark suit in a bright office"></div>
  <h1 class="abs hero" style="all:unset;position:absolute;left:116px;top:183px;font:600 27px 'Open Sans',sans-serif;color:#1a7fb8;letter-spacing:1px">IT CONSULTING FIRM</h1>
  <p class="abs hero-lead">Should you CHOOSE TO HAVE A cus­tomized greeting on your ACCOUNT, WE WILL NOT .</p>
  <p class="abs hero-body">Lorem Ipsum is simply dummy text of the pring and typesetting industry. Lorem Ipsum has been the industry's standard.when an unknownLorem Ipsum has been the industry's standard dummy text....</p>
  <div class="abs btn-learn">Learn More »</div>
  <div class="abs dots"><i></i><i class="on"></i><i></i><i></i></div>
</section>

<section>
  <div class="abs svc" style="left:91px">
    <h2>IT SUPPORT</h2>
    <p class="txt">Lorem Ipsum is simply dummy text of the pring and typesetting industry. Lorem Ipsum has been the industry's standard.</p>
    <p class="txt" style="margin-top:11px">when an unknownLorem Ipsum has been the industry's standard dummy text....</p>
    <span class="more">View more</span>
  </div>
  <div class="abs svc" style="left:366px">
    <h2>IT SERVICES</h2>
    <ul>
      <li><svg width="12" height="11" viewBox="0 0 12 11"><path d="M1 6l3 3 7-8" fill="none" stroke="#fff" stroke-width="2.2"/></svg>Lorem Ipsum is simply dummy text of the</li>
      <li><svg width="12" height="11" viewBox="0 0 12 11"><path d="M1 6l3 3 7-8" fill="none" stroke="#fff" stroke-width="2.2"/></svg>Lorem Ipsum is simply dummy text of the</li>
      <li><svg width="12" height="11" viewBox="0 0 12 11"><path d="M1 6l3 3 7-8" fill="none" stroke="#fff" stroke-width="2.2"/></svg>Lorem Ipsum is simply dummy text of the</li>
      <li><svg width="12" height="11" viewBox="0 0 12 11"><path d="M1 6l3 3 7-8" fill="none" stroke="#fff" stroke-width="2.2"/></svg>Lorem Ipsum is simply dummy text of the</li>
    </ul>
    <span class="more">View more</span>
  </div>
  <div class="abs svc" style="left:642px">
    <h2>IT SOLUTIONS</h2>
    <ul style="line-height:11.5px">
      <li><svg width="13" height="13" viewBox="0 0 13 13"><path d="M3 12V7a3 3 0 013-3h5M8 1l3 3-3 3" fill="none" stroke="#fff" stroke-width="2"/></svg>Lorem Ipsum is simply dummy text of the printing and typesetting industry.</li>
      <li><svg width="13" height="13" viewBox="0 0 13 13"><path d="M3 12V7a3 3 0 013-3h5M8 1l3 3-3 3" fill="none" stroke="#fff" stroke-width="2"/></svg>Lorem Ipsum is simply dummy text of the printing and typesetting industry.</li>
      <li><svg width="13" height="13" viewBox="0 0 13 13"><path d="M3 12V7a3 3 0 013-3h5M8 1l3 3-3 3" fill="none" stroke="#fff" stroke-width="2"/></svg>Lorem Ipsum is simply dummy text of the printing and typesetting industry.</li>
    </ul>
    <span class="more">View more</span>
  </div>
</section>

<section class="abs content"></section>
<h3 class="abs h3" style="left:105px;top:699px">Latest News</h3>
<h3 class="abs h3" style="left:355px;top:699px">Recent Tweets</h3>
<h3 class="abs h3" style="left:595px;top:699px">Our Client’s are Awesome</h3>
<div class="abs news-title">Lorem ipsum dolor sit amet</div>
<div class="abs news-date">14<sup style="font-size:6px">th</sup> November</div>
<p class="abs news-body">Nam libero tempore, cum soluta nobis est eligendi optio cumque nihil impedit quo lorem ipsum dolor sit &nbsp;minus id quod maxime placeat facere possimus, omnis voluptas assumenda est, omnis dolor repellendus...</p>
<div class="abs news-more">FULL ARTICLE &nbsp;›</div>
<div class="abs tweets">
  <div class="tweet"><b>@quietcoder</b> Lorem ipsum dolor sit amet consectetur adipisicing elit.<small>9 hours ago</small></div>
  <div class="tweet"><b>@bluefern</b> At vero eos et accusamus et iusto odio dignissimos ducimus blanditiis praesentium voluptatum<small>1 day ago</small></div>
</div>
<div class="abs qdots"><i></i><i></i><i style="background:#555"></i></div>
<div class="abs quote">At vero eos et accusamus et lucero iusto odio dignissimos ducimus qui blanditiis praesentium voluptatum deleniti atque corrupti quos dolores et quas molestias excepturi sint occaecati cupiditate non provident.<span class="mark">”</span></div>
<div class="abs quote-by"><b style="font-weight:600">John Doe</b>, <span>xyz etc.</span>, cat lover</div>

<section class="abs cta"></section>
<div class="abs cta-big">BUILD YOUR BRAND. GET STARTED HERE</div>
<div class="abs cta-small">or call us &nbsp;&nbsp;(800) 555-0142</div>
<div class="abs cta-btn">Request A Quote</div>

<footer class="abs footer"></footer>
<div class="abs mapframe"></div>
<div class="abs map" role="img" aria-label="Street map of the office area"></div>
<div class="abs addr" style="left:254px;top:1049px"><b>IT Services North, Harbour Area</b><br>120 Lantern Row Suite 210<br>Brookvale, Westland 40521</div>
<div class="abs addr" style="left:255px;top:1097px"><b>IT Services North, Harbour Area</b><br>120 Lantern Row Suite 210<br>Brookvale, Westland 40521</div>
<div class="abs ft-link" style="left:331px;top:1146px">Contact Us &gt;&gt;</div>
<div class="abs soc" style="left:480px;top:1044px"><span class="ic" style="background:#35558f"></span><div class="t"><b>Facenote</b>Join the Convesation!<br>Connect With us &gt;&gt;</div></div>
<div class="abs soc" style="left:482px;top:1106px"><span class="ic" style="background:#46b5e6"></span><div class="t"><b>Chirper</b>see what we’re up to.<br>Follow Us &gt;&gt;</div></div>
<div class="abs soc" style="left:668px;top:1044px">
  <svg class="ic" width="42" height="42" viewBox="0 0 42 42"><rect width="42" height="42" rx="6" fill="#f39a2b"/><rect x="8" y="12" width="26" height="18" fill="#fff"/><path d="M8 12l13 10 13-10" fill="none" stroke="#f39a2b" stroke-width="1.5"/></svg>
  <div class="t" style="margin-top:-2px"><b>News &amp; Tips your Inbox</b></div>
</div>
<div class="abs nl"><svg style="position:absolute;right:10px;top:3px" width="14" height="14" viewBox="0 0 14 14"><circle cx="5.5" cy="5.5" r="4" fill="none" stroke="#ddd" stroke-width="1.5"/><path d="M8.5 8.5l4 4" stroke="#ddd" stroke-width="2"/></svg></div>
<div class="abs soc" style="left:668px;top:1106px"><span class="ic" style="background:#1b86c2"></span><div class="t"><b>ProLink</b>Add us to your<br>Professional network.<br>follow Us &gt;&gt;</div></div>
<div class="abs footbar">© 2012 • IT Services • All Rights Reserved</div>

</body>
</html>
```